Vehicle Design

I would like the Van done with the logo and things that we do it need to look professional,
The link it to a car site for a 2003 VH Orvane Kestrel this is the same as i have so hope you can use the photos of here, or get the specs that you need, I have a sign person that does all my vehicles, so will need to pass the winning file to him,
Target Market(s)
mobile advertising police and housing
Industry/Entity Type
It Professional
Requirements
Must have
- logo, phone number 0468 357 921 what we do link attached,was hopping to have emblem on doors at rear, and sides done with style
Should be discrete but still make a noise
Nice to have
- Smoke that is in card that is attached
Should not have
- should not be too much not to scare clients from having me outside,

```html
<!DOCTYPE html>
<html lang="en">
<head>
<meta charset="utf-8">
<title>Veritas Scene Restoration Crew – Van Side Signage</title>
<link rel="stylesheet" href="https://fonts.googleapis.com/css2?family=Federo&family=Tinos&family=Rokkitt:wght@700&display=swap">
<style>
  :root {
    --canvas: #f2f2f0;
    --panel-yellow: #f9c416;
    --ink-brown: #3b2a0e;
    --ink-black: #151515;
  }
  * { margin: 0; padding: 0; box-sizing: border-box; }
  html, body { width: 1200px; height: 666px; overflow: hidden; }
  body { background: var(--canvas); position: relative; }

  .sign-panel {
    position: absolute;
    background: var(--panel-yellow);
  }
  .brand-panel {
    left: 100px; top: 150px; width: 461px; height: 211px;
    display: flex; flex-direction: column; align-items: center; justify-content: center;
    gap: 18px;
  }
  .brand-mark {
    width: 64px; height: 64px; border-radius: 50%;
    background: var(--ink-black);
  }
  .brand-name {
    font-family: "Federo", sans-serif;
    color: var(--ink-brown);
    font-size: 30px; line-height: 1.05;
    text-transform: uppercase; text-align: center; letter-spacing: 0.5px;
  }

  .services-panel {
    left: 566px; top: 148px; width: 542px; height: 199px;
    padding: 16px 24px 0 40px;
  }
  .service-list {
    list-style: none;
    font-family: "Tinos", serif;
    color: var(--ink-brown);
    font-size: 19px; line-height: 32px;
  }
  .service-list li::before { content: "•"; }

  .phone-line {
    position: absolute; left: 180px; top: 455px;
    display: flex; align-items: center; gap: 22px;
  }
  .phone-icon { width: 56px; height: 56px; }
  .phone-number {
    font-family: "Rokkitt", serif; font-weight: 700;
    color: var(--ink-black);
    font-size: 76px; letter-spacing: 2px; line-height: 1;
  }
</style>
</head>
<body>
  <section class="sign-panel brand-panel">
    <span class="brand-mark"></span>
    <p class="brand-name">Veritas Scene<br>Restoration Crew</p>
  </section>

  <section class="sign-panel services-panel">
    <ul class="service-list">
      <li>Mould Inspections and Remediation •Crime and Trauma Scene Cleanup and Decontamination</li>
      <li>Drug Lab Decontamination and Needle Cleanups</li>
      <li>Odour control •Air Quality Testing and Swabs</li>
      <li>Hydroxyl Machine, Ozone Machine, Sterilising Light</li>
    </ul>
  </section>

  <div class="phone-line">
    <svg class="phone-icon" viewBox="0 0 56 56" aria-hidden="true">
      <circle cx="28" cy="28" r="27" fill="var(--ink-black)"/>
      <circle cx="28" cy="28" r="21" fill="var(--panel-yellow)"/>
      <path d="M21 15c2-1 4 0 5 2l2 4c1 2 0 3-1 4l-2 1c1 3 3 6 6 8l2-2c1-1 3-1 4 0l3 3c1 2 1 4-1 5-3 2-7 2-11-1-5-4-9-9-10-15-1-4 1-8 3-9z" fill="var(--ink-black)"/>
    </svg>
    <span class="phone-number">0468 357 921</span>
  </div>
</body>
</html>
```